BUSINESS CARD - HALVERDINE RURAL SERVICES

I would like to create a business card for my fertilizer spreading business. I would like to incorporate my existing logo and also a description of the services offered. The business card will be given to farmers so must be kept simple but effective. It will also be left in stores so much also be eye catching in order to stand out from other cards.

Target Market(s)

FARMERS

Requirements
Must have
• FRONT OF CARD = EXISTING LOGO + "CUSTOMISED SPREADING" below the logo

REAR Of CARD = SERVICES OFFERED AND CONTACT DETAILS

- Bulk fertilizer including Lime, Gypsum, Manure & Compost
- Granular fertilizer including Single Super, Urea, Gran-am, & Custom Blends
- Modern equipment - Autosteer & Variable Rate Capable
- Friendly & Reliable Service
- Contact Gus: 0471 502 318
Nice to have
• utilize same color scheme as existing logo

```html
<!DOCTYPE html>
<html lang="en">
<head>
<meta charset="utf-8">
<title>Halverdine Rural Services – Business Card</title>
<link rel="stylesheet" href="https://fonts.googleapis.com/css2?family=Lato:wght@400;700;900&display=swap">
<style>
  :root {
    --stage: #2f3236;
    --card-white: #ffffff;
    --card-black: #0b0b0b;
    --orange: #f7941d;
    --charcoal: #4a4a4a;
    --text: #3d3d3d;
    --logo-grey: #6b6b6b;
  }
  * { margin: 0; padding: 0; box-sizing: border-box; }
  html, body {
    width: 1200px; height: 900px; overflow: hidden;
    background: var(--stage);
    font-family: "Lato", Arial, sans-serif;
  }
  .canvas {
    width: 1200px; height: 900px;
    display: flex; align-items: center; justify-content: center;
    gap: 40px;
  }
  .card {
    position: relative;
    width: 540px; height: 310px;
    border-radius: 16px;
    overflow: hidden;
    box-shadow: 0 14px 30px rgba(0,0,0,.45);
  }
  /* Rear card */
  .card--rear { background: var(--card-white); }
  .card__wave { position: absolute; inset: 0; width: 100%; height: 100%; }
  .contact { position: absolute; top: 24px; left: 34px; z-index: 1; }
  .contact__name { font-weight: 700; font-size: 19px; color: var(--text); }
  .contact__role { font-size: 14px; color: var(--orange); margin-top: 1px; }
  .contact__phone {
    display: flex; align-items: center; gap: 6px;
    font-size: 15px; color: var(--text); margin-top: 2px;
  }
  .contact__phone svg { width: 13px; height: 13px; }
  .services {
    position: absolute; top: 110px; left: 34px; z-index: 1;
    list-style: none; font-size: 15px; line-height: 1.35; color: var(--text);
  }
  .services li { position: relative; padding-left: 18px; }
  .services li::before {
    content: ""; position: absolute; left: 0; top: 5px;
    width: 11px; height: 11px; border-radius: 50%; background: var(--orange);
  }
  .services li.no-bullet::before { display: none; }
  /* Front card */
  .card--front {
    background: var(--card-black);
    display: flex; align-items: center; justify-content: center; gap: 16px;
  }
  .brand__dot {
    width: 64px; height: 64px; border-radius: 50%; background: var(--logo-grey);
  }
  .brand__name {
    font-weight: 900; font-size: 34px; line-height: 1.05;
    color: var(--logo-grey); letter-spacing: -0.5px;
  }
</style>
</head>
<body>
<main class="canvas">
  <section class="card card--rear" aria-label="Rear of business card">
    <svg class="card__wave" viewBox="0 0 540 310" preserveAspectRatio="none" aria-hidden="true">
      <path d="M0 224 C130 232 270 286 540 292 L540 310 L0 310 Z" fill="var(--charcoal)"/>
      <path d="M0 233 C130 242 270 294 540 299 L540 310 L0 310 Z" fill="var(--card-white)"/>
      <path d="M0 242 C130 254 270 302 540 305 L540 310 L0 310 Z" fill="var(--orange)"/>
    </svg>
    <div class="contact">
      <p class="contact__name">Gus</p>
      <p class="contact__role">ceo / General Manager</p>
      <p class="contact__phone">
        <svg viewBox="0 0 24 24" aria-hidden="true"><path fill="var(--orange)" d="M6.6 10.8a15.1 15.1 0 0 0 6.6 6.6l2.2-2.2a1 1 0 0 1 1-.25 11.4 11.4 0 0 0 3.6.57 1 1 0 0 1 1 1V20a1 1 0 0 1-1 1A17 17 0 0 1 3 4a1 1 0 0 1 1-1h3.5a1 1 0 0 1 1 1c0 1.25.2 2.45.57 3.6a1 1 0 0 1-.25 1z"/></svg>
        0471 502 318
      </p>
    </div>
    <ul class="services">
      <li>Bulk fertilizer including Lime, Gypsum, Manure &amp; Compost.</li>
      <li>Granular fertilizer including Single Super,</li>
      <li>Urea, Gran-am, &amp; Custom Blends.</li>
      <li>Modern equipment - Autosteer &amp; Variable Rate Capable.</li>
      <li class="no-bullet">Friendly &amp; Reliable Service.</li>
    </ul>
  </section>

  <section class="card card--front" aria-label="Front of business card">
    <span class="brand__dot" aria-hidden="true"></span>
    <p class="brand__name">Halverdine Rural<br>Services</p>
  </section>
</main>
</body>
</html>
```